Vyntra Ad Design for Culinary Toursim Company

Looking for ad design for www.savorlanewalks.example to be used on VYNTRA traffic ads.

Below is one example of the

We are looking for vyntra ad design
Post: 1080x1080 with text,
Stories: 1080x1920 with text

Text should read
Food For Thought
CTA: Join our {CITY} Food Tour

Logo and optional photos are attached. You can edit the photos as you see fit.
Brand guidelines https://www.filevault.example/s/k3m9q2x7/Savor-Lane-Walks-Brand-Guidelines.docx

Logos https://www.filevault.example/f/r8t4w1z6/logos

Target Market(s)

United States Foodies ages 30-65

Industry/Entity Type

Tourism

Font styles to use
Other font styles liked:
• Avenir

Requirements
Must have
• High Design
Nice to have
• See Brand Guidelines
Should not have
• See Brand Guidelines

```html
<!DOCTYPE html>
<html lang="en">
<head>
<meta charset="utf-8">
<title>Savor Lane Walks – Food For Thought ads</title>
<link rel="stylesheet" href="https://fonts.googleapis.com/css2?family=Nunito+Sans:wght@700;800;900&display=swap">
<style>
  :root {
    --board-grey: #737273;
    --paper: #ffffff;
    --paper-fade: #e4e4e5;
    --brand-red: #a51e23;
    --brand-red-deep: #8a1519;
    --band-red: #8e1a1d;
    --ink: #231f20;
    --label-white: #ffffff;
    --photo-dark: #3a2f27;
    --photo-warm: #b98a55;
  }
  * { margin: 0; padding: 0; box-sizing: border-box; }
  html, body { width: 1200px; height: 988px; overflow: hidden; }
  body {
    background: var(--board-grey);
    font-family: "Nunito Sans", "Avenir Next", Avenir, sans-serif;
    position: relative;
  }
  .ad {
    position: absolute;
    overflow: hidden;
    background: linear-gradient(180deg, var(--paper) 0%, var(--paper) 28%, var(--paper-fade) 70%, #d6d6d7 100%);
  }
  .ad--post { left: 62px; top: 61px; width: 575px; height: 575px; }
  .ad--story { left: 660px; top: 61px; width: 467px; height: 831px; }

  .brand {
    position: absolute;
    display: flex;
    align-items: center;
    gap: 8px;
    color: var(--ink);
    font-weight: 800;
    line-height: 1.05;
  }
  .brand__dot {
    flex: none;
    border-radius: 50%;
    background: var(--brand-red);
  }
  .ad--post .brand { left: 32px; top: 74px; width: 150px; font-size: 21px; }
  .ad--post .brand__dot { width: 26px; height: 26px; }
  .ad--story .brand { left: 34px; top: 68px; width: 124px; font-size: 17px; }
  .ad--story .brand__dot { width: 21px; height: 21px; }

  .headline { position: absolute; font-weight: 900; white-space: nowrap; line-height: 1; }
  .headline__food { position: absolute; color: var(--brand-red); letter-spacing: -1px; }
  .headline__for { position: absolute; color: var(--ink); font-weight: 800; }
  .headline__thought { position: absolute; color: var(--ink); letter-spacing: -1px; }

  .ad--post .headline { left: 0; top: 0; }
  .ad--post .headline__food { left: 209px; top: 30px; font-size: 85px; }
  .ad--post .headline__for { left: 453px; top: 79px; font-size: 25px; }
  .ad--post .headline__thought { left: 238px; top: 100px; font-size: 63px; }

  .ad--story .headline__food { left: 168px; top: 32px; font-size: 69px; color: var(--brand-red-deep); }
  .ad--story .headline__for { left: 371px; top: 71px; font-size: 19px; }
  .ad--story .headline__thought { left: 188px; top: 89px; font-size: 53px; }

  .photo-frame {
    position: absolute;
    background: var(--paper);
    padding: 6px;
    box-shadow: 0 14px 14px -8px rgba(0,0,0,0.45);
  }
  .photo-frame__image {
    width: 100%; height: 100%;
    background:
      radial-gradient(ellipse at 55% 85%, var(--photo-warm) 0%, rgba(185,138,85,0) 55%),
      linear-gradient(180deg, #4a4038 0%, var(--photo-dark) 45%, #6e5438 100%);
  }
  .ad--post .photo-frame { left: 36px; top: 186px; width: 507px; height: 304px; }
  .ad--story .photo-frame { left: 33px; top: 182px; width: 403px; height: 539px; padding: 5px; }

  .cta {
    position: absolute;
    background: var(--band-red);
    color: var(--label-white);
    font-weight: 800;
    text-align: center;
    white-space: nowrap;
    border-radius: 28px 28px 0 0;
    letter-spacing: 0.3px;
  }
  .ad--post .cta { left: 67px; top: 525px; width: 441px; height: 50px; font-size: 29px; line-height: 52px; }
  .ad--story .cta { left: 38px; top: 775px; width: 397px; height: 56px; font-size: 26px; line-height: 58px; }

  .size-label {
    position: absolute;
    color: var(--label-white);
    font-weight: 800;
    font-size: 37px;
    line-height: 1;
    white-space: nowrap;
  }
  .size-label--post { left: 206px; top: 646px; }
  .size-label--story { left: 788px; top: 896px; }
</style>
</head>
<body>
  <section class="ad ad--post" aria-label="Square post ad">
    <div class="brand"><span class="brand__dot"></span><span>Savor Lane Walks</span></div>
    <h1 class="headline">
      <span class="headline__food">FOOD</span>
      <span class="headline__for">FOR</span>
      <span class="headline__thought">THOUGHT</span>
    </h1>
    <div class="photo-frame">
      <div class="photo-frame__image" role="img" aria-label="Cook plating a dish at a warmly lit restaurant counter with fries, grilled meat and salad"></div>
    </div>
    <div class="cta">JOIN OUR CITY FOOD TOUR</div>
  </section>
  <div class="size-label size-label--post">1080X1080PX</div>

  <section class="ad ad--story" aria-label="Story ad">
    <div class="brand"><span class="brand__dot"></span><span>Savor Lane Walks</span></div>
    <h1 class="headline">
      <span class="headline__food">FOOD</span>
      <span class="headline__for">FOR</span>
      <span class="headline__thought">THOUGHT</span>
    </h1>
    <div class="photo-frame">
      <div class="photo-frame__image" role="img" aria-label="Close view of a cook pouring sauce over a plate in a restaurant kitchen"></div>
    </div>
    <div class="cta">JOIN OUR CITY FOOD TOUR</div>
  </section>
  <div class="size-label size-label--story">1080X1920PX</div>
</body>
</html>
```